Design a new letterhead

We need a new letterhead as our current one is looking a bit boring. We're a tech company but would prefer not to have clipart or cheap looking graphics on our letterhead as we are trying to give off a professional, corporate image.

Our colours are very straightforward, blue (#24b8dc) and white, however we do also use black, and we do not mind using a darker shade of blue also if it looks better. Sticking to these colours would be preferred, however if you can make another colour look good as well, that would be fine.

I've attached both of our logos, one in blue, one in white. Our logo/tagline must, obviously feature somewhere on the letterhead. I've also attached our image-only logo which can be used as a secondary item on the letterhead if required.

The letterhead must also include the following details:

Our Phone numbers which are:

0508-374-915
09-681-4357

Our website and email which are:

www.vbl.net.nz
contact@vbl.net.nz

Our address which is:

17 Harlowby Lane
Birkenhead, Auckland 0626

Please feel free to ask if you have any questions or queries regarding this competition.

```html
<!DOCTYPE html>
<html lang="en">
<head>
<meta charset="utf-8">
<title>Verbello Letterhead</title>
<link rel="stylesheet" href="https://fonts.googleapis.com/css2?family=Nunito:wght@700&family=Open+Sans:wght@400;600&family=Tinos&display=swap">
<style>
  :root {
    --brand-blue: #24b8dc;
    --brand-blue-pale: #e3f5fa;
    --ink: #222222;
    --muted: #6f7478;
    --footer-grey: #8d9398;
    --paper: #ffffff;
    --backdrop: #eceded;
  }
  * { box-sizing: border-box; margin: 0; padding: 0; }
  html, body { width: 1200px; height: 795px; overflow: hidden; }
  body { background: var(--backdrop); position: relative; }

  .letterhead {
    position: absolute;
    left: 333px; top: 20px;
    width: 534px; height: 755px;
    background: var(--paper);
    overflow: hidden;
    box-shadow: 0 2px 10px rgba(0,0,0,0.08);
  }

  .backdrop-circle {
    position: absolute;
    right: -150px; top: 250px;
    width: 380px; height: 380px;
    border-radius: 50%;
    background: var(--brand-blue-pale);
  }

  .contact-block {
    position: absolute;
    right: 40px; top: 38px;
    text-align: right;
    font-family: "Open Sans", sans-serif;
    font-size: 6.5px;
    line-height: 10px;
    color: var(--muted);
  }
  .contact-block li { list-style: none; }
  .contact-block li::after {
    content: "";
    display: inline-block;
    width: 5px; height: 5px;
    margin-left: 5px;
    background: var(--brand-blue);
    vertical-align: middle;
  }
  .contact-block li.address-line::after { background: transparent; }

  .brand {
    position: absolute;
    left: 40px; top: 132px;
    display: flex; align-items: center; gap: 6px;
  }
  .brand-dot {
    width: 22px; height: 22px; border-radius: 50%;
    background: var(--brand-blue);
  }
  .brand-name {
    font-family: "Nunito", sans-serif;
    font-weight: 700;
    font-size: 21px;
    color: var(--brand-blue);
    line-height: 1;
  }
  .brand-tagline {
    font-family: "Nunito", sans-serif;
    font-weight: 700;
    font-size: 5px;
    color: var(--brand-blue);
    margin-top: 2px;
    letter-spacing: 0.2px;
  }

  .letter {
    position: absolute;
    left: 62px; top: 200px;
    width: 360px;
    font-family: "Tinos", serif;
    font-size: 8.6px;
    line-height: 10.6px;
    color: var(--ink);
  }
  .letter p { margin-bottom: 10px; }
  .sender-block { margin-bottom: 18px; }

  .signature {
    width: 70px; height: 24px;
    margin: 4px 0 2px;
    background: linear-gradient(90deg, rgba(34,34,34,0.18), rgba(34,34,34,0.05));
    border-radius: 3px;
  }

  .footer-band {
    position: absolute;
    left: 0; bottom: 0;
    width: 100%; height: 60px;
  }
  .footer-web {
    position: absolute;
    right: 22px; bottom: 14px;
    font-family: "Open Sans", sans-serif;
    font-weight: 600;
    font-size: 8px;
    color: var(--paper);
    letter-spacing: 0.4px;
  }
</style>
</head>
<body>
  <main class="letterhead">
    <div class="backdrop-circle" aria-hidden="true"></div>

    <ul class="contact-block">
      <li class="address-line">17 Harlowby Lane</li>
      <li class="address-line">Birkenhead, Auckland 0626</li>
      <li>0508-374-915</li>
      <li>09-681-4357</li>
      <li>www.vbl.net.nz</li>
      <li>contact@vbl.net.nz</li>
    </ul>

    <div class="brand">
      <div class="brand-dot" aria-hidden="true"></div>
      <div>
        <div class="brand-name">Verbello</div>
        <div class="brand-tagline">Smart IT solutions for business</div>
      </div>
    </div>

    <article class="letter">
      <div class="sender-block">
        [Your Name]<br>
        [Street Address]<br>
        [City, ST &nbsp;ZIP Code]<br>
        [Date]April 16, 2014
      </div>

      <p>Dear [Recipient Name]:</p>

      <p>Kestrel Analytics employed Marisa Tolland full-time as a senior editor. For more than four years she managed the content and delivery of our monthly internal newsletter. Her recent layoff was the direct result of an initiative at Kestrel Analytics to downsize during this slow economic quarter. Last month, Kestrel Analytics closed its editorial department indefinitely.</p>

      <p>Marisa is an intelligent and motivated individual. She is more than capable of managing a small group of people. As senior editor, Marisa recruited and managed one writer and one copyeditor. With the help of this team, she produced a high-quality newsletter every month and never missed a deadline.</p>

      <p>As part of her former responsibilities, Marisa interviewed competitors in our sector and developed reports on new technologies and areas for growth. Peers in my field would often tell me that Marisa was interesting to talk to and wrote credible copy that accurately reflected their feedback. I believe that developing quality relationships with industry competitors is the responsibility of each Kestrel Analytics employee, and Marisa's consistent contributions to that end are an excellent case in point.</p>

      <p>If you would like additional information about Marisa, you can telephone me at (425) 555-0193.</p>

      <p>Sincerely,</p>
      <div class="signature" role="img" aria-label="Handwritten signature of Ned Farrow"></div>
    </article>

    <svg class="footer-band" viewBox="0 0 534 60" preserveAspectRatio="none" aria-hidden="true">
      <path d="M0 44 C180 40 300 30 380 18 C430 10 480 4 534 2 L534 60 L0 60 Z" fill="var(--footer-grey)"/>
      <path d="M0 50 C200 47 320 40 400 30 C450 24 495 20 534 19 L534 60 L0 60 Z" fill="var(--brand-blue)"/>
    </svg>
    <div class="footer-web">www.vbl.net.nz</div>
  </main>
</body>
</html>
```